Presentation Folder, for Cancer Awareness, VERY COLORFULL AND MODERN

This will be a standard size folder that will hold standard 8 1/2 x 11 papers with a business card slot on the flap, this is a very easy project with very little text and the design for the back page is already done so all you really have to do is make a very nice colorful front cover, you will see my attachments are labeled and I gave you alot of instructions, this should be a very fast easy project

Reason: there has not been enough quality designs, sorry

Target Market(s)

Our Target Market is Dr's that Deal with Cancer patients

Industry/Entity Type

Healthcare

Font styles to use
Serif

Colors

Designer to choose colors to be used in the design.

Requirements
Must have
• Project must be tasteful and look professional with the ribbons as the main focal point in the center of folder the folder should be a nice gray color to accent the color of the ribbons , the back page needs no design it is the" Kestrel Test" in the attachments I sent
Nice to have
• I would like the ribbons displayed in a row, I included a logo sample layout
• a picture on the front of the folder under the words Hereditary Cancer Screening - Then under that put the words - The Power of Knowledge - then add the picture I labeled Great Picture in the attachments

```html
<!DOCTYPE html>
<html lang="en">
<head>
<meta charset="utf-8">
<title>Hereditary Cancer Screening Folder</title>
<link rel="stylesheet" href="https://fonts.googleapis.com/css2?family=Montserrat:wght@300;400;800&family=Lato:wght@400;700&family=Courier+Prime&display=swap">
<style>
  :root {
    --red: #e0423a;
    --magenta: #e8198b;
    --ink: #555a5e;
    --slate: #5f6468;
    --flap: #98999c;
    --rule: #b9bbbe;
    --zebra: #ececed;
    --lynch: #f6c32e;
    --peutz: #b6c73e;
    --li: #3fae4e;
    --cowden: #1b9ad6;
    --gastric: #5a5d5e;
  }
  * { margin: 0; padding: 0; box-sizing: border-box; }
  html, body { width: 1200px; height: 959px; overflow: hidden; background: #fff; }
  body { position: relative; font-family: "Lato", sans-serif; color: var(--ink); }
  .dieline { position: absolute; inset: 0; }
  .abs { position: absolute; }

  /* Back panel: test menu */
  .menu-title { left: 45px; width: 551px; top: 30px; text-align: center; font-family: "Lato", sans-serif; font-size: 31px; color: var(--red); letter-spacing: 0.5px; }
  .menu-title sup { font-size: 12px; vertical-align: 16px; }
  .menu-sub { left: 45px; width: 551px; top: 63px; text-align: center; font-size: 12.5px; letter-spacing: 1.2px; color: #888; }
  .gene-table { left: 133px; top: 94px; width: 378px; border: 1px solid #777; }
  .row { display: flex; height: 12.85px; align-items: center; font-size: 8.6px; letter-spacing: 0.5px; }
  .row:nth-child(even) { background: var(--zebra); }
  .row .gene { width: 123px; padding-left: 10px; color: var(--red); }
  .row .organ { flex: 1; color: #666; }
  .row.small { font-size: 7px; }
  .head { display: flex; height: 12.85px; align-items: center; font-size: 9.5px; font-weight: 700; color: #fff; letter-spacing: 0.6px; }
  .head .gene { width: 123px; padding-left: 10px; background: var(--red); height: 100%; display: flex; align-items: center; }
  .head .organ { flex: 1; padding-left: 10px; background: var(--slate); height: 100%; display: flex; align-items: center; }
  .band { height: 12.85px; display: flex; align-items: center; padding-left: 12px; font-size: 9px; font-weight: 700; color: #fff; letter-spacing: 0.7px; }
  .band.lynch { background: var(--lynch); }
  .band.peutz { background: var(--peutz); }
  .band.li { background: var(--li); }
  .band.cowden { background: var(--cowden); }
  .band.gastric { background: var(--gastric); }

  .back-brand { left: 45px; width: 551px; top: 633px; display: flex; justify-content: center; align-items: center; gap: 6px; font-size: 9px; letter-spacing: 2.5px; color: var(--red); }
  .dot { display: inline-block; border-radius: 50%; background: var(--red); }
  .back-brand .dot { width: 14px; height: 14px; }
  .contact { left: 131px; width: 382px; top: 655px; display: flex; justify-content: space-between; font-size: 5.6px; color: #666; letter-spacing: 0.2px; }

  /* Front cover */
  .brand { left: 598px; width: 554px; top: 48px; display: flex; flex-direction: column; align-items: center; gap: 8px; }
  .brand .dot { width: 34px; height: 34px; }
  .brand .name { font-size: 16px; letter-spacing: 4px; color: var(--red); }
  .headline { left: 598px; width: 554px; top: 131px; text-align: center; font-family: "Montserrat", sans-serif; font-weight: 800; color: var(--magenta); font-size: 35px; line-height: 32px; letter-spacing: 0.3px; }
  .tagline { left: 598px; width: 554px; top: 205px; text-align: center; font-family: "Montserrat", sans-serif; font-weight: 300; font-size: 27px; letter-spacing: 7.4px; color: #6d7073; }
  .ribbons { left: 621px; top: 270px; width: 505px; height: 118px; border-radius: 6px;
    background: linear-gradient(90deg, #f5e35a, #c3c3c5, #f2a1bd, #4fc7c8, #a98be0, #3446d8, #7a4a1e, #f08b94, #7cbf3d, #2e76d6, #e4e4e4, #222, #8fd1f0, #8fa2ef); }
  .photo { left: 598px; top: 400px; width: 554px; height: 296px;
    background: linear-gradient(160deg, #d9d2c8 0%, #b9a48a 40%, #8a6a4b 70%, #c9c0b3 100%); }
  .photo-band { left: 598px; top: 666px; width: 554px; height: 30px; background: rgba(45,45,45,0.8); color: #fff; font-family: "Montserrat", sans-serif; font-weight: 400; font-size: 22px; letter-spacing: 9px; text-align: center; line-height: 30px; }

  /* Flaps (printed upside down) */
  .flip { transform: rotate(180deg); color: #fff; font-family: "Courier Prime", monospace; text-align: center; }
  .partner { left: 168px; width: 300px; top: 906px; }
  .partner .lead { font-size: 13px; }
  .partner .sub { font-size: 9.5px; margin-top: 2px; }
  .pitch { left: 720px; width: 360px; top: 772px; font-size: 11.6px; line-height: 15.6px; }
</style>
</head>
<body>

<svg class="dieline" width="1200" height="959" viewBox="0 0 1200 959" aria-hidden="true">
  <g fill="none" stroke="#c9cbcd" stroke-width="0.8">
    <path d="M45 10 H4 V424 A14 14 0 0 1 4 452 V690 H45"/>
    <path d="M1152 10 H1196 V424 A14 14 0 0 0 1196 452 V690 H1152"/>
    <line x1="45" y1="4" x2="1152" y2="4" stroke-dasharray="2 3"/>
    <line x1="597" y1="4" x2="597" y2="696" stroke-dasharray="2 3"/>
  </g>
  <path d="M48 696 H596 L560 936 Q556 956 534 956 H48 Z" fill="var(--flap)"/>
  <path d="M602 696 H1150 V956 H664 Q644 956 640 936 Z" fill="var(--flap)"/>
  <g stroke="#fff" stroke-width="1">
    <line x1="216" y1="800" x2="251" y2="766"/>
    <line x1="388" y1="766" x2="423" y2="800"/>
    <line x1="214" y1="852" x2="251" y2="888"/>
    <line x1="424" y1="852" x2="388" y2="888"/>
  </g>
</svg>

<!-- Back panel -->
<div class="abs menu-title">KESTREL<sup>™</sup> Test Menu</div>
<div class="abs menu-sub">CLIA# 00D0000000 &nbsp;| GENVISTA-LAB.COM</div>

<div class="abs gene-table">
  <div class="head"><span class="gene">GENE</span><span class="organ">CANCER-ASSOCIATED ORGAN/SYSTEMS</span></div>
  <div>
    <div class="row"><span class="gene">APC</span><span class="organ">Colon</span></div>
    <div class="row"><span class="gene">ATM</span><span class="organ">Breast/Pancreatic/Brain</span></div>
    <div class="row"><span class="gene">BARD1</span><span class="organ">Breast/Ovarian</span></div>
    <div class="row"><span class="gene">BMPR1A</span><span class="organ">Colon</span></div>
    <div class="row"><span class="gene">BRCA1</span><span class="organ">Breast/Ovarian/Prostate</span></div>
    <div class="row"><span class="gene">BRCA2</span><span class="organ">Breast/Ovarian/Prostate</span></div>
    <div class="row"><span class="gene">BRIP1</span><span class="organ">Breast/Ovarian</span></div>
    <div class="row"><span class="gene">CDK4</span><span class="organ">Melanoma</span></div>
    <div class="row"><span class="gene">P16 (CDKN2A)</span><span class="organ">Melanoma/Breast/Pancreatic/Squamous</span></div>
    <div class="row"><span class="gene">FANCC</span><span class="organ">Blood</span></div>
    <div class="row"><span class="gene">MEN1</span><span class="organ">Thyroid/Parathyroid</span></div>
    <div class="row"><span class="gene">MET</span><span class="organ">Renal/Hepatic</span></div>
    <div class="row"><span class="gene">MRE11A</span><span class="organ">Ovarian/Breast</span></div>
    <div class="row"><span class="gene">NBN</span><span class="organ">Breast/Ovarian/Prostate/Melanoma</span></div>
    <div class="row"><span class="gene">NF1</span><span class="organ">Blood</span></div>
    <div class="row"><span class="gene">NTRK1</span><span class="organ">Thyroid/Parathyroid</span></div>
    <div class="row"><span class="gene">PALB2</span><span class="organ">Breast/Ovarian/Pancreatic</span></div>
    <div class="row"><span class="gene">PTCH1</span><span class="organ">Melanoma/Brain/Breast/Colon</span></div>
    <div class="row"><span class="gene">RAD50</span><span class="organ">Breast/Ovarian</span></div>
    <div class="row"><span class="gene">RAD51C</span><span class="organ">Ovarian/Breast</span></div>
    <div class="row"><span class="gene">RAD51D</span><span class="organ">Ovarian/Breast</span></div>
    <div class="row"><span class="gene">RET</span><span class="organ">Lung/Thyroid/Parathyroid</span></div>
    <div class="row"><span class="gene">SMAD4</span><span class="organ">Colon/Pancreas</span></div>
  </div>
  <div class="band lynch">LYNCH SYNDROME GENES</div>
  <div>
    <div class="row small"><span class="gene">MLH1</span><span class="organ">Colorectal/Ovarian</span></div>
    <div class="row small"><span class="gene">MSH2</span><span class="organ">Colorectal/Ovarian</span></div>
    <div class="row small"><span class="gene">MSH6</span><span class="organ">Colorectal/Ovarian</span></div>
    <div class="row small"><span class="gene">PMS2</span><span class="organ">Colorectal/Ovarian</span></div>
    <div class="row small"><span class="gene">EPCAM</span><span class="organ">Colorectal</span></div>
  </div>
  <div class="band peutz">PEUTZ-JEGHERS SYNDROME GENE</div>
  <div><div class="row small"><span class="gene">STK11</span><span class="organ">Breast/Ovarian/Melanoma/Colorectal/Lung</span></div></div>
  <div class="band li">LI-FRAUMENI SYNDROME GENE</div>
  <div>
    <div class="row small"><span class="gene">CHEK2</span><span class="organ">Breast/Ovarian/Prostate</span></div>
    <div class="row small"><span class="gene">TP53</span><span class="organ">Breast/Bladder/Ovarian/Squamous</span></div>
  </div>
  <div class="band cowden">COWDEN SYNDROME GENE</div>
  <div><div class="row small"><span class="gene">PTEN</span><span class="organ">Endometrium/Breast/Prostate/Lung</span></div></div>
  <div class="band gastric">HEREDITARY DIFFUSE GASTRIC CANCER SYNDROME GENE</div>
  <div>
    <div class="row small"><span class="gene">CDH1</span><span class="organ">Breast/Gastric/Ovarian/Prostate</span></div>
    <div class="row small"><span class="gene">VHL</span><span class="organ">Renal</span></div>
  </div>
</div>

<div class="abs back-brand"><span class="dot"></span><span>GENVISTA</span></div>
<div class="abs contact">
  <span>2200 MAPLE RIDGE AVE NW | SUITE B | SPRINGFIELD, GA 30000</span>
  <span>(tel) 555.010.4821 | (fax) 555.010.4822 | hello@genvista-lab.com</span>
</div>

<!-- Front cover -->
<div class="abs brand"><span class="dot"></span><span class="name">GENVISTA</span></div>
<h1 class="abs headline">HEREDITARY<br>CANCER SCREENING</h1>
<div class="abs tagline">The Power of Knowledge</div>
<div class="abs ribbons" role="img" aria-label="A row of fourteen overlapping cancer awareness ribbons in many colours"></div>
<div class="abs photo" role="img" aria-label="Photo of a multi-generation family sharing a meal at an outdoor table"></div>
<div class="abs photo-band">TYPES OF CANCER</div>

<!-- Flaps -->
<div class="abs flip partner">
  <div class="lead">Harbor Health Partners</div>
  <div class="sub">an independent arm of GenVista LLC</div>
</div>
<div class="abs flip pitch">
  At our state of the art, CLIA certified and COLA<br>
  accredited facility we perform Next Generation Sequencing<br>
  (NGS) based screening for mutations known to affect<br>
  an individual's Risk of developing Hereditary Cancer.<br>
  Results from the test enable the Physician to make<br>
  Better informed treatment decisions.
</div>

</body>
</html>
```